Improve My Resume Design to be easier for the reader and the recruiter

I need to improve my resume design to make it easier to read and attract employer eyes in a very professional way. And the graphs should be neat, nice and professional. - You can use the below logos as the companies that I worked with are so famous.

Detailed information about me is inside the CV.

Target Market(s)

Big Companies and Famous recruiters

Industry/Entity Type

Government

Colors

Designer to choose colors to be used in the design.

Requirements
Must have
• Infographics .. Easy to Read.
Nice to have
• Charts, infographics.
Should not have
• not professional colours.

```html
<!DOCTYPE html>
<html lang="en">
<head>
<meta charset="utf-8">
<title>Khalid Yousef Omar Nasser — Resume</title>
<link rel="stylesheet" href="https://fonts.googleapis.com/css2?family=Oswald:wght@300;500;600&family=Open+Sans:wght@400;700&display=swap">
<style>
  :root{
    --yellow:#dfca27;
    --ink:#111111;
    --paper-top:#ececec;
    --paper:#f8f8f8;
    --stage:#e6e6e6;
    --white:#ffffff;
    --head:'Oswald', 'Arial Narrow', sans-serif;
    --body:'Open Sans', Arial, sans-serif;
  }
  *{margin:0;padding:0;box-sizing:border-box}
  html,body{width:1200px;height:1200px;overflow:hidden;background:var(--stage)}
  .resume{position:absolute;left:176px;top:0;width:939px;height:1329px;transform:scale(0.9029);transform-origin:0 0;background:var(--paper);overflow:hidden;font-family:var(--body);color:var(--ink)}
  .abs{position:absolute}
  .intro-bg{left:0;top:0;width:483px;height:392px;background:var(--paper-top)}
  .side{left:483px;top:0;width:456px;height:1329px;background:var(--ink)}
  .frame-top{left:483px;top:203px;width:119px;height:64px;background:var(--yellow)}
  .frame-right{left:538px;top:203px;width:64px;height:441px;background:var(--yellow)}
  .frame-bottom{left:0;top:580px;width:602px;height:64px;background:var(--yellow)}
  .name-first{left:23px;top:14px;font:300 54px/1 var(--head);letter-spacing:-0.5px}
  .name-last{left:23px;top:72px;font:600 58px/1 var(--head);color:var(--yellow)}
  .role-tag{left:23px;top:152px;height:42px;padding:0 8px;background:var(--ink);color:var(--white);font:500 18px/42px var(--head);letter-spacing:-0.3px}
  .summary{left:25px;top:200px;width:443px;font-size:14.3px;line-height:19px;text-align:justify}
  .contact{left:0;height:34px;display:flex;align-items:center}
  .contact .icon{width:67px;height:34px;background:var(--yellow);display:flex;align-items:center;justify-content:center}
  .contact .label{height:34px;background:var(--ink);color:var(--white);font:700 20px/34px var(--body);padding:0 12px}
  .contact .value{font:700 20px/34px var(--body);margin-left:21px}
  .section-band{left:64px;top:589px;font:600 34px/46px var(--head);letter-spacing:-0.5px}
  .date-tag{left:23px;width:189px;height:51px;background:var(--yellow);font:500 23px/51px var(--head);text-align:center;letter-spacing:-0.5px}
  .job{left:23px;width:445px;font-size:17px;line-height:23px}
  .job strong{font-weight:700}
  .job-notes{left:23px;top:1203px;width:445px;font-size:12.5px;line-height:17px}
  .facts{left:483px;top:35px;width:456px}
  .fact{position:absolute;width:110px;text-align:center;color:var(--yellow);font:500 19px/20px var(--head);letter-spacing:-0.3px}
  .fact svg{display:block;margin:0 auto 14px}
  .side-head{font:600 33px/1 var(--head);color:var(--yellow);letter-spacing:-0.5px}
  .edu-text{left:620px;top:244px;width:290px;color:var(--white);font-size:11.2px;line-height:15px}
  .skills{left:624px;top:364px;list-style:none;color:var(--white);font-size:14.5px;line-height:23.7px}
  .skills li{display:flex;align-items:center;gap:9px}
  .dev{left:504px;top:729px;width:415px;list-style:none;color:var(--white);font-size:16px;line-height:21px}
  .dev li{display:flex;gap:14px;margin-bottom:20px}
  .dev svg{flex:none;margin-top:3px}
  .prev-text{left:505px;top:1239px;width:420px;color:var(--white);font-size:16px;line-height:21px}
</style>
</head>
<body>
<main class="resume">
  <div class="abs intro-bg"></div>
  <div class="abs side"></div>
  <div class="abs frame-top"></div>
  <div class="abs frame-right"></div>
  <div class="abs frame-bottom"></div>

  <h1 class="abs name-first">KHALID YOUSEF</h1>
  <div class="abs name-last">OMAR NASSER</div>
  <div class="abs role-tag">SENIOR PROJECT MANAGER</div>
  <p class="abs summary">Dedicated and multi-faceted professional with advanced analytical, reasoning and problem-solving skills, and offering over 13 years' insightful experience performing investigative research and analysis to address tactical and strategic business challenges. Adept in the field of Project Management since 6 years with core skills in managing IT &amp; Non-IT Projects, CST Projects etc. Seeking an opportunity to leverage excellent project management, business analysis and data analytics skills and experience with a reputed organization to contribute to strategic business planning</p>

  <div class="abs contact" style="top:415px">
    <span class="icon"><svg width="14" height="22" viewBox="0 0 14 22"><rect x="1.5" y="1.5" width="11" height="19" rx="2" fill="none" stroke="#111" stroke-width="2.5"/><circle cx="7" cy="17" r="1.3" fill="#111"/></svg></span>
    <span class="label">PHONE</span><span class="value">+971 500 123 456</span>
  </div>
  <div class="abs contact" style="top:468px">
    <span class="icon"><svg width="26" height="18" viewBox="0 0 26 18"><rect x="1" y="1" width="24" height="16" fill="none" stroke="#111" stroke-width="2"/><path d="M1 1 13 10 25 1M1 17l9-8M25 17l-9-8" fill="none" stroke="#111" stroke-width="2"/></svg></span>
    <span class="label">EMAIL</span><span class="value">k.nasser84@mailbox.com</span>
  </div>
  <div class="abs contact" style="top:521px">
    <span class="icon"><svg width="22" height="20" viewBox="0 0 22 20"><path d="M11 1 1 10h3v9h5v-6h4v6h5v-9h3z" fill="#111"/></svg></span>
    <span class="label">LOCATION</span><span class="value">Dubai, UAE</span>
  </div>

  <h2 class="abs section-band">PROFESSIONAL EXPERIENCE</h2>

  <div class="abs date-tag" style="top:670px">MAR 2017 - PRESENT</div>
  <div class="abs job" style="top:735px"><strong>FEDERAL OFFICE FOR CIVIL WORKFORCE SERVICES (FOCWS), DUBAI, UAE</strong><br>Senior Consultant - Human Resources Systems (Project Management Office)</div>

  <div class="abs date-tag" style="top:849px">DEC 2011 - FEB 2017</div>
  <div class="abs job" style="top:913px"><strong>MERIDIAN UPSTREAM IRAQ HOLDING B.V., DUBAI, UAE</strong><br>Head – Corporate Affairs <strong>(Dec 2012 - Feb 2017)</strong><br>Executive - Performance &amp; Reporting, Business Planning &amp; Commercial Dept., Planning Unit<br><strong>(Dec 2011 – Dec 2012)</strong></div>

  <div class="abs date-tag" style="top:1076px">JUL 2007 - DEC 2011</div>
  <div class="abs job" style="top:1140px"><strong>COASTAL CITY MUNICIPALITY, DUBAI, UAE</strong><br>IT CONSULTANT</div>
  <p class="abs job-notes">Business Analyst - e-Transformation Section, Strategic Planning &amp; Innovation Unit <strong>(Aug 2010 - Dec 2011)</strong><br>• Sr. Building System Analyst - Building Dept., Prequalification &amp; Building Studies Section, Support Unit <strong>(Aug 2008 - Jul 2010)</strong><br>• Business Support Engineer - e-Government Services Section, Support Unit <strong>(Jul 2007 - JUL 2008)</strong></p>

  <div class="abs facts">
    <div class="fact" style="left:6px">
      <svg width="84" height="84" viewBox="0 0 84 84"><circle cx="42" cy="42" r="39" fill="none" stroke="#dfca27" stroke-width="4"/><path d="M42 22c-8 0-14 6-14 14 0 10 14 26 14 26s14-16 14-26c0-8-6-14-14-14z" fill="#fff"/><circle cx="42" cy="36" r="5" fill="#111"/></svg>
      JORDANIAN</div>
    <div class="fact" style="left:118px">
      <svg width="84" height="84" viewBox="0 0 84 84"><circle cx="42" cy="42" r="39" fill="none" stroke="#dfca27" stroke-width="4"/><g fill="#fff"><rect x="24" y="40" width="36" height="18" rx="2"/><rect x="27" y="32" width="4" height="8"/><rect x="35" y="32" width="4" height="8"/><rect x="45" y="32" width="4" height="8"/><rect x="53" y="32" width="4" height="8"/><circle cx="29" cy="27" r="2"/><circle cx="37" cy="27" r="2"/><circle cx="47" cy="27" r="2"/><circle cx="55" cy="27" r="2"/></g></svg>
      24TH OCT<br>1984</div>
    <div class="fact" style="left:226px">
      <svg width="84" height="84" viewBox="0 0 84 84"><circle cx="42" cy="42" r="39" fill="none" stroke="#dfca27" stroke-width="4"/><circle cx="44" cy="46" r="17" fill="none" stroke="#fff" stroke-width="3"/><path d="M26 26l5-5 6 6-5 5z" fill="none" stroke="#fff" stroke-width="2.5"/></svg>
      MARRIED</div>
    <div class="fact" style="left:336px">
      <svg width="84" height="84" viewBox="0 0 84 84"><circle cx="42" cy="42" r="39" fill="none" stroke="#dfca27" stroke-width="4"/><g fill="none" stroke="#fff" stroke-width="3"><circle cx="42" cy="40" r="19"/><ellipse cx="42" cy="40" rx="8" ry="19"/><path d="M23 40h38M26 31h32M26 49h32"/></g></svg>
      ENGLISH &amp;<br>ARABIC</div>
  </div>

  <h2 class="abs side-head" style="left:620px;top:203px">EDUCATION</h2>
  <p class="abs edu-text">Master's Degree in Information Technology Management, Harbourview University, Dubai, UAE <strong>(2010)</strong><br>B Sc. (Computer Science), Karak Valley University, Jordan <strong>(2006)</strong></p>

  <h2 class="abs side-head" style="left:620px;top:323px">CORE COMPETENCIES</h2>
  <ul class="abs skills">
    <li><svg width="13" height="12" viewBox="0 0 13 12"><path d="M0 0 13 6 0 12 3 6z" fill="#dfca27"/></svg>Leadership &amp; Team Building</li>
    <li><svg width="13" height="12" viewBox="0 0 13 12"><path d="M0 0 13 6 0 12 3 6z" fill="#dfca27"/></svg>Business/IT Analysis</li>
    <li><svg width="13" height="12" viewBox="0 0 13 12"><path d="M0 0 13 6 0 12 3 6z" fill="#dfca27"/></svg>Requirements Gathering/Analysis</li>
    <li><svg width="13" height="12" viewBox="0 0 13 12"><path d="M0 0 13 6 0 12 3 6z" fill="#dfca27"/></svg>Business Consulting</li>
    <li><svg width="13" height="12" viewBox="0 0 13 12"><path d="M0 0 13 6 0 12 3 6z" fill="#dfca27"/></svg>Project Management</li>
    <li><svg width="13" height="12" viewBox="0 0 13 12"><path d="M0 0 13 6 0 12 3 6z" fill="#dfca27"/></svg>Issues And Crisis Management</li>
    <li><svg width="13" height="12" viewBox="0 0 13 12"><path d="M0 0 13 6 0 12 3 6z" fill="#dfca27"/></svg>Business Process Re-engineering</li>
    <li><svg width="13" height="12" viewBox="0 0 13 12"><path d="M0 0 13 6 0 12 3 6z" fill="#dfca27"/></svg>System/Services Support</li>
    <li><svg width="13" height="12" viewBox="0 0 13 12"><path d="M0 0 13 6 0 12 3 6z" fill="#dfca27"/></svg>Client / Stakeholder Management</li>
    <li><svg width="13" height="12" viewBox="0 0 13 12"><path d="M0 0 13 6 0 12 3 6z" fill="#dfca27"/></svg>Event Management</li>
    <li><svg width="13" height="12" viewBox="0 0 13 12"><path d="M0 0 13 6 0 12 3 6z" fill="#dfca27"/></svg>Reporting &amp; Documentation</li>
    <li><svg width="13" height="12" viewBox="0 0 13 12"><path d="M0 0 13 6 0 12 3 6z" fill="#dfca27"/></svg>Business Process Mapping</li>
  </ul>

  <h2 class="abs side-head" style="left:504px;top:678px;font-size:36px">PROFESSIONAL DEVELOPMENT</h2>
  <ul class="abs dev">
    <li><svg width="18" height="18" viewBox="0 0 18 18"><path d="M15 6.5A7 7 0 1 1 12 3" fill="none" stroke="#dfca27" stroke-width="2"/><path d="M5.5 8.5l3 3L16 3" fill="none" stroke="#dfca27" stroke-width="2"/></svg><span>Nimbus Certified Professional (NCP) in Developing Nimbus WebForms Applications Using Nimbus Studio</span></li>
    <li><svg width="18" height="18" viewBox="0 0 18 18"><path d="M15 6.5A7 7 0 1 1 12 3" fill="none" stroke="#dfca27" stroke-width="2"/><path d="M5.5 8.5l3 3L16 3" fill="none" stroke="#dfca27" stroke-width="2"/></svg><span>Certified Business Analysis Practitioner (CBAC) Certificate</span></li>
    <li><svg width="18" height="18" viewBox="0 0 18 18"><path d="M15 6.5A7 7 0 1 1 12 3" fill="none" stroke="#dfca27" stroke-width="2"/><path d="M5.5 8.5l3 3L16 3" fill="none" stroke="#dfca27" stroke-width="2"/></svg><span>Nimbus EPM 2010 Portfolio Management and Business Analysts Training</span></li>
    <li><svg width="18" height="18" viewBox="0 0 18 18"><path d="M15 6.5A7 7 0 1 1 12 3" fill="none" stroke="#dfca27" stroke-width="2"/><path d="M5.5 8.5l3 3L16 3" fill="none" stroke="#dfca27" stroke-width="2"/></svg><span>Atlas 8.0 Essentials Ed1 Certificate from Vantor University (20 Sep 2011 Until 28th Sep 2011)</span></li>
    <li><svg width="18" height="18" viewBox="0 0 18 18"><path d="M15 6.5A7 7 0 1 1 12 3" fill="none" stroke="#dfca27" stroke-width="2"/><path d="M5.5 8.5l3 3L16 3" fill="none" stroke="#dfca27" stroke-width="2"/></svg><span>Vantor Database Course</span></li>
    <li><svg width="18" height="18" viewBox="0 0 18 18"><path d="M15 6.5A7 7 0 1 1 12 3" fill="none" stroke="#dfca27" stroke-width="2"/><path d="M5.5 8.5l3 3L16 3" fill="none" stroke="#dfca27" stroke-width="2"/></svg><span>IT - Web Development Training</span></li>
    <li><svg width="18" height="18" viewBox="0 0 18 18"><path d="M15 6.5A7 7 0 1 1 12 3" fill="none" stroke="#dfca27" stroke-width="2"/><path d="M5.5 8.5l3 3L16 3" fill="none" stroke="#dfca27" stroke-width="2"/></svg><span>Introduction to Nimbus Basic Programming</span></li>
    <li><svg width="18" height="18" viewBox="0 0 18 18"><path d="M15 6.5A7 7 0 1 1 12 3" fill="none" stroke="#dfca27" stroke-width="2"/><path d="M5.5 8.5l3 3L16 3" fill="none" stroke="#dfca27" stroke-width="2"/></svg><span>Many Oil &amp; Gas Conferences and Seminars in Malaysia and Iraq</span></li>
  </ul>

  <h2 class="abs side-head" style="left:504px;top:1193px;font-size:36px">PREVIOUS ASSIGNMENT</h2>
  <p class="abs prev-text">Web Developer, Cedarline Integrated Solutions Company, Amman, Jordan <strong>(Jul 2006 - Jun 2007)</strong></p>
</main>
</body>
</html>
```